New Look Driving School Project

Current website:
www. kelmorawheelacademy.com

Websites that we like (use content and courses from here as well):
https://www. tollbenroadclass.com

We are looking for a fresh looking driving school website that is easy for students to find the course they are looking for, the price, and allow them to book a lesson all on our website. We would like for this website to have multiple pages: Home, Teen Courses, Adult Courses, About Us, Contact, FAQ, Blog, Requirements.

Target Market(s)

Students in High School or Parents

Industry/Entity Type

Education

Coding

Coded - Design and coding required

Number of Pages Required

5+ page

Font styles to use
Serif
Sans Serif

Colors

Designer to choose colors to be used in the design.

Requirements
Must have
• Must have a form submission and payment processing option. Must have the ability to pick a course, see available times, and process their payment online. MUST BE MOBILE FRIENDLY DESIGN.
Nice to have
• Nice to have a clean format, with big bold fonts.
Should not have
• Should not have a lot of sliders or animations. Should be very fast loading on mobile. Keep it simple but easy to read and elegant.

```html
<!DOCTYPE html>
<html lang="en">
<head>
<meta charset="utf-8">
<title>Kelmora Wheel Academy</title>
<link href="https://fonts.googleapis.com/css2?family=Montserrat:ital,wght@0,400;0,500;0,600;0,700;0,800;1,400&family=Oswald:wght@500;600&family=Dancing+Script:wght@700&display=swap" rel="stylesheet">
<style>
:root{
  --red:#e42a2d;
  --navy:#16213a;
  --navy-2:#1d2a47;
  --ink:#1c2436;
  --text:#6b7280;
  --line:#e3e6ec;
  --white:#ffffff;
  --pale:#f6f7fa;
}
*{box-sizing:border-box;margin:0;padding:0}
html,body{width:1200px;height:4945px;overflow:hidden}
body{font-family:"Montserrat",sans-serif;color:var(--ink);background:var(--white);position:relative}
.abs{position:absolute}
.btn{display:inline-block;background:var(--red);color:var(--white);font-weight:600;font-size:13px;text-align:center;line-height:40px;height:40px;padding:0 30px;border-radius:2px;white-space:nowrap}
.btn-dark{background:var(--navy)}
.section-title{font-weight:700;font-size:30px;text-align:center;line-height:1.3;color:var(--navy)}
.small{font-size:12px;line-height:1.7;color:var(--text)}

/* hero */
.hero{top:0;left:0;width:1200px;height:593px;background:linear-gradient(115deg,#1a2438 0%,#2e3b52 40%,#55606f 70%,#2a3244 100%)}
.nav{top:28px;left:150px;display:flex;gap:30px;font-size:13px;font-weight:500;color:var(--white)}
.topcall{top:22px;left:850px;color:var(--red);font-weight:700;font-size:14px}
.topcall span{display:block;color:#c9ced8;font-weight:400;font-size:11px;margin-top:2px}
.brand{top:104px;left:138px;display:flex;align-items:center;gap:10px;color:var(--white);font-weight:700;font-size:16px}
.brand i{width:14px;height:14px;background:var(--red);border-radius:50%}
.hero-title{top:178px;left:138px;color:var(--white);font-weight:700;font-size:46px;line-height:1.15}
.hero-text{top:306px;left:138px;width:430px;color:#e6e9ef;font-size:14px;line-height:1.6}
.hero-text b{color:var(--white)}
.booking{top:72px;left:781px;width:281px;height:406px;background:var(--white);padding:22px 22px;box-shadow:0 8px 30px rgba(0,0,0,.25)}
.booking h3{font-family:"Dancing Script",cursive;color:var(--red);font-size:32px;text-align:center;line-height:1}
.booking p{text-align:center;font-size:13px;font-weight:600;color:var(--navy);margin:4px 0 16px}
.field{height:36px;border:1px solid var(--line);font-size:11px;color:#9aa0ab;padding:0 12px;line-height:34px;margin-bottom:12px}
.row{display:flex;gap:10px}
.row .field{flex:1}
.booking .btn{width:100%;padding:0;margin-top:2px}
.strip{top:544px;left:0;width:1200px;height:49px;background:rgba(14,20,34,.85);color:#c8cdd6;font-size:12px;line-height:49px;padding-left:138px;display:flex;align-items:center;gap:16px}
.strip b{color:var(--red);font-weight:600}
.strip .learn{position:absolute;left:933px;top:12px;height:26px;line-height:24px;width:129px;border:1px solid #8a90a0;color:var(--white);font-size:11px;text-align:center}

/* specialties */
.spec-title{top:640px;left:0;width:1200px}
.spec-card{top:758px;width:282px;height:198px;background:linear-gradient(135deg,#7d8aa0,#b8c2cf);color:var(--white);font-weight:700;font-size:15px;display:flex;align-items:center;justify-content:center;text-align:center;padding:0 40px}
.spec-mid{background:var(--white);border:3px solid var(--red);flex-direction:column;color:var(--text);font-weight:400;font-size:12px;line-height:1.6;padding:0 34px;box-shadow:0 10px 30px rgba(0,0,0,.15)}
.spec-mid .btn{height:30px;line-height:30px;font-size:11px;padding:0 20px;margin-top:12px}
.trees{top:956px;left:0;width:1200px;height:165px;background:linear-gradient(180deg,#dfe5ea 0%,#7d9483 55%,#3f5a49 100%)}

/* programs */
.programs{top:1121px;left:0;width:1200px;height:676px;background:var(--navy)}
.programs .section-title{color:var(--white);position:absolute;top:40px;width:100%;font-size:28px}
.programs .sub{position:absolute;top:86px;width:100%;text-align:center;color:#b9c0cd;font-size:13px}
.prog{background:linear-gradient(135deg,#5b6678,#a3acb9);color:var(--white);padding:24px}
.prog .days{font-size:10px;font-weight:600;letter-spacing:.5px}
.prog h4{font-size:16px;font-weight:700;line-height:1.3;margin-top:4px}
.prog .btn{height:28px;line-height:26px;font-size:11px;padding:0 16px;background:transparent;border:1px solid var(--white);margin-top:12px}
.price{width:66px;height:66px;border-radius:50%;background:var(--red);color:var(--white);font-weight:700;font-size:17px;display:flex;align-items:center;justify-content:center;border:3px solid var(--white)}

/* why */
.why-title{top:1842px;left:0;width:1200px}
.feature{top:1958px;width:220px;text-align:center}
.feature h5{font-size:14px;font-weight:700;margin:12px 0 10px}
.why-btn{top:2162px;left:520px}

/* about */
.city{top:2268px;left:0;width:1200px;height:462px;background:linear-gradient(180deg,#f0a24a 0%,#d2804a 35%,#5f6f7e 70%,#3b4a5a 100%)}
.about-box{top:2407px;left:138px;width:597px;height:395px;background:var(--white);padding:56px 60px;box-shadow:0 10px 40px rgba(0,0,0,.15)}
.about-box h2{font-size:28px;font-weight:700;line-height:1.25;margin-bottom:20px}
.about-box .btn{margin-top:26px}

/* stats */
.stat{top:2920px;width:300px;text-align:center}
.stat b{display:block;font-family:"Oswald",sans-serif;font-weight:600;color:var(--red);font-size:40px}
.stat span{font-size:14px;color:var(--ink)}

/* reviews */
.review-photo{top:3191px;left:0;width:1200px;height:462px;background:linear-gradient(120deg,#3d4a5d 0%,#7a8796 45%,#5c6676 100%)}
.review-box{top:3109px;left:462px;width:600px;height:396px;background:var(--white);box-shadow:0 10px 40px rgba(0,0,0,.18);text-align:center;padding:40px 70px}
.review-box h2{font-size:28px;font-weight:700;margin-bottom:20px}
.review-box q{display:block;font-style:italic;font-size:14px;line-height:1.7;color:var(--text);quotes:"\201C" "\201D"}
.avatar{width:56px;height:56px;border-radius:50%;background:#8a6a58;margin:24px auto 8px}
.stars{color:var(--red);font-size:14px;letter-spacing:2px}
.arrow{position:absolute;top:215px;color:#9aa0ab;font-size:20px}

/* cta */
.cta{top:3653px;left:0;width:1200px;height:188px;background:var(--red);color:var(--white);padding:56px 138px}
.cta h2{font-size:30px;font-weight:700}
.cta p{font-size:14px;margin-top:4px}
.cta .btn{position:absolute;left:781px;top:74px;width:281px;padding:0}

/* blog & faq */
.foggy{top:4270px;left:0;width:1200px;height:180px;background:linear-gradient(180deg,#ffffff 0%,#e6e9ee 100%)}
.col-title{font-size:20px;font-weight:700}
.post{top:3940px;width:202px;height:346px;background:var(--white);box-shadow:0 6px 24px rgba(0,0,0,.12)}
.post .pic{height:164px;background:linear-gradient(135deg,#e05a35,#f4b36b)}
.post .pic.alt{background:linear-gradient(135deg,#59606b,#b9bec6)}
.post .meta{font-size:10px;color:#9aa0ab;padding:18px 20px 6px}
.post h6{font-size:14px;font-weight:600;color:var(--red);line-height:1.4;padding:0 20px}
.faq{top:3960px;left:620px;width:442px}
.faq-item{display:flex;gap:12px;font-size:14px;font-weight:600;padding:11px 0;border-bottom:1px solid var(--line)}
.faq-item i{font-style:normal;width:18px;height:18px;border:1.5px solid var(--ink);border-radius:50%;font-size:13px;line-height:14px;text-align:center;flex:none}
.faq-item.open{color:var(--red);border:0;padding-bottom:6px}
.faq-item.open i{border-color:var(--red)}
.faq .answer{font-size:12px;line-height:1.7;color:var(--text);padding:0 0 12px 30px;border-bottom:1px solid var(--line)}

/* footer */
.footer{top:4450px;left:0;width:1200px;height:495px;background:var(--navy);color:#c2c8d3}
.footer h3{position:absolute;font-size:20px;font-weight:700;color:var(--white)}
.call{position:absolute;left:138px;top:150px;font-size:24px;color:var(--white)}
.call b{color:var(--red);font-weight:700}
.addr{position:absolute;left:138px;top:190px;font-size:12px;line-height:1.7}
.social{position:absolute;left:138px;top:290px;display:flex;gap:14px}
.social i{width:16px;height:16px;background:#c2c8d3;border-radius:3px}
.copy{position:absolute;left:138px;top:412px;font-size:11px}
.qfield{position:absolute;height:40px;border:1px solid #3a4866;font-size:11px;color:#8c94a5;padding:0 14px;line-height:38px}
.footer .btn{position:absolute;left:620px;top:405px;height:38px;line-height:38px;padding:0 40px}
</style>
</head>
<body>

<header class="hero abs" role="img" aria-label="Photo of a student driver behind the wheel with an instructor"></header>
<nav class="nav abs"><span>Home</span><span>Teen Courses</span><span>Adult Courses</span><span>About</span><span>FAQ</span><span>Blog</span><span>Contact</span></nav>
<div class="topcall abs">Call: 555-014-3872<span>Mon - Fri: 8.00 AM - 5.00 PM</span></div>
<div class="brand abs"><i></i>Kelmora Certified</div>
<h1 class="hero-title abs">Kelmora Wheel<br>Academy</h1>
<p class="hero-text abs">We are experts in teen driving education in <b>Fairfax</b>, <b>Chantilly</b>, <b>Centreville</b>, and <b>Herndon</b> and the greater <b>Northern Virginia</b> area.</p>
<span class="btn abs" style="top:400px;left:138px">Contact Us Today</span>

<form class="booking abs">
  <h3>Schedule</h3>
  <p>Your Driving Course!</p>
  <div class="field">Enter your Name</div>
  <div class="field">Email</div>
  <div class="field">Phone</div>
  <div class="field">Course &#9662;</div>
  <div class="row"><div class="field">Date</div><div class="field">Time</div></div>
  <span class="btn">Book Now!</span>
</form>

<div class="strip abs">
  <svg width="22" height="16" viewBox="0 0 22 16"><path d="M3 9l2-6h12l2 6v5h-3v-2H6v2H3z" fill="none" stroke="#fff" stroke-width="1.5"/></svg>
  <span>We care about the <b>success of our students and our goal</b> is to help you learn and become a safe driver.</span>
  <span class="learn">Learn More &#8594;</span>
</div>

<h2 class="section-title abs spec-title">Kelmora Wheel Academy specializes<br>in Behind the Wheel for</h2>
<div class="trees abs" role="img" aria-label="Road lined with pine trees and a passing car"></div>
<div class="spec-card abs" style="left:138px" role="img" aria-label="Photo of a smiling teen driver">Teen and Adult Drivers</div>
<div class="spec-card spec-mid abs" style="left:461px">Our lessons build calm, confident drivers with patient coaching on real roads every step of the way.<span class="btn">More Info</span></div>
<div class="spec-card abs" style="left:780px" role="img" aria-label="Photo of an instructor with a student">Driver Education and Training</div>

<section class="programs abs">
  <h2 class="section-title">Choose Your Program</h2>
  <p class="sub">that best fits your schedule and goals in our Driving School.</p>
</section>
<div class="prog abs" style="top:1279px;left:138px;width:439px;height:435px;padding-top:300px" role="img" aria-label="Photo of a smiling adult driver">
  <div class="days">60 DAYS</div><h4>Driving Adult Waiver<br>program</h4><span class="btn">More Info</span>
</div>
<div class="prog abs" style="top:1279px;left:610px;width:452px;height:198px;padding-top:80px;padding-left:36px" role="img" aria-label="Photo of an instructor teaching in a car">
  <div class="days">30 DAYS</div><h4>Behind the Wheel<br>Driving</h4>
</div>
<div class="prog abs" style="top:1517px;left:610px;width:214px;height:197px;padding-top:110px" role="img" aria-label="Photo of a young woman driving">
  <div class="days">14 DAYS</div><h4>Private Car<br>Driving</h4>
</div>
<div class="prog abs" style="top:1517px;left:847px;width:215px;height:197px;padding-top:110px" role="img" aria-label="Photo of hands on a steering wheel">
  <div class="days">14 DAYS</div><h4>Drivers Training<br>Education</h4>
</div>
<div class="price abs" style="top:1255px;left:118px">$600</div>
<div class="price abs" style="top:1255px;left:592px">$250</div>
<div class="price abs" style="top:1494px;left:592px">$400</div>
<div class="price abs" style="top:1494px;left:830px">$150</div>

<h2 class="section-title abs why-title">Why Choose<br>Kelmora Wheel Academy</h2>
<div class="feature abs" style="left:137px">
  <svg width="34" height="34" viewBox="0 0 34 34"><path d="M17 3l11 4v9c0 7-5 12-11 15C11 28 6 23 6 16V7z" fill="none" stroke="#e42a2d" stroke-width="2"/><path d="M12 17l4 4 7-8" fill="none" stroke="#e42a2d" stroke-width="2"/></svg>
  <h5>100% Guarantee</h5><p class="small">We guarantee 100% satisfaction and premium training from our instructors</p>
</div>
<div class="feature abs" style="left:390px">
  <svg width="34" height="34" viewBox="0 0 34 34"><circle cx="17" cy="17" r="8" fill="none" stroke="#e42a2d" stroke-width="2"/><circle cx="17" cy="17" r="14" fill="none" stroke="#e42a2d" stroke-width="2" stroke-dasharray="4 3"/></svg>
  <h5>Affordable</h5><p class="small">You have nothing to worry about, as our services are affordable and flexible</p>
</div>
<div class="feature abs" style="left:622px">
  <svg width="34" height="34" viewBox="0 0 34 34"><circle cx="17" cy="12" r="6" fill="none" stroke="#e42a2d" stroke-width="2"/><path d="M7 30c1-6 5-9 10-9s9 3 10 9" fill="none" stroke="#e42a2d" stroke-width="2"/></svg>
  <h5>Experience</h5><p class="small">We offer proven lessons and customer training</p>
</div>
<div class="feature abs" style="left:856px">
  <svg width="34" height="34" viewBox="0 0 34 34"><circle cx="17" cy="11" r="6" fill="none" stroke="#e42a2d" stroke-width="2"/><path d="M9 30l3-12h10l3 12M13 23h8" fill="none" stroke="#e42a2d" stroke-width="2"/></svg>
  <h5>Certified Trainer</h5><p class="small">All of our instructors are certified by the State Department of Motor Vehicles</p>
</div>
<span class="btn abs why-btn">Contact Us Today!</span>

<div class="city abs" role="img" aria-label="City skyline at sunset"></div>
<div class="about-box abs">
  <h2>About Kelmora Wheel<br>Academy</h2>
  <p class="small">We are experts in teen driving education in Fairfax, Chantilly, Centreville, and Herndon and the greater Northern Virginia area. Kelmora Wheel Academy specializes in Behind the Wheel for Teens and Adults, License Permits and Drivers Education. Our friendly team plans each lesson around the student, keeps every class small and focused, and helps new drivers gain real road confidence quickly.</p>
  <span class="btn">About Us</span>
</div>

<div class="stat abs" style="left:130px"><b>100%</b><span>Satisfaction Guaranteed</span></div>
<div class="stat abs" style="left:410px"><b>20,000</b><span>Hours of Teaching</span></div>
<div class="stat abs" style="left:773px"><b>Free</b><span>Pick Up and Drop Off</span></div>

<div class="review-photo abs" role="img" aria-label="Photo of an instructor handing over car keys to a driver"></div>
<div class="review-box abs">
  <h2>Reviews</h2>
  <q>The instructor was very knowledgeable and informative. Every lesson felt calm and clear, and I passed on my first try. I would recommend this Driving School to anyone and everyone!</q>
  <div class="avatar" role="img" aria-label="Reviewer portrait"></div>
  <div style="font-size:13px;font-weight:600">Mara Ellison</div>
  <div class="stars">&#9733;&#9733;&#9733;&#9733;&#9733;</div>
  <span class="arrow" style="left:200px">&#8249;</span><span class="arrow" style="right:200px">&#8250;</span>
</div>

<section class="cta abs">
  <h2>Schedule Your Driving Programs</h2>
  <p>We offer very FLEXIBLE schedules and timings for any student.</p>
  <span class="btn btn-dark">Schedule Your Courses Today!</span>
</section>

<div class="foggy abs" role="img" aria-label="Soft misty landscape"></div>
<h3 class="col-title abs" style="top:3862px;left:138px">Latest Blog</h3>
<article class="post abs" style="left:138px">
  <div class="pic" role="img" aria-label="Red sports car on a dusty road"></div>
  <div class="meta">18 APR, 2019</div>
  <h6>Tips for your first lesson on busy city roads</h6>
</article>
<article class="post abs" style="left:379px">
  <div class="pic alt" role="img" aria-label="Man driving a car"></div>
  <div class="meta">18 APR, 2019</div>
  <h6>How to stay calm during your road test day</h6>
</article>
<span class="btn abs" style="top:4370px;left:138px;height:34px;line-height:34px;font-size:11px;padding:0 24px">View All</span>

<h3 class="col-title abs" style="top:3862px;left:620px">Frequently Asked Questions</h3>
<div class="faq abs">
  <div class="faq-item open"><i>&minus;</i>How long is the road test appointment?</div>
  <p class="answer">We ask a parent or guardian that signs up the form. Teens must hold a learner permit for at least nine months and complete 45 hours of supervised driving, with 15 hours after dark.</p>
  <div class="faq-item"><i>+</i>I'm 18 years old, can I get my Driver License?</div>
  <div class="faq-item"><i>+</i>This is an accordion for FAQ Module?</div>
  <div class="faq-item"><i>+</i>How do I obtain a Commercial Driver License?</div>
  <div class="faq-item"><i>+</i>What is the process for getting my class?</div>
</div>
<span class="btn abs" style="top:4370px;left:620px;height:34px;line-height:34px;font-size:11px;padding:0 28px">More</span>

<footer class="footer abs">
  <h3 style="left:138px;top:67px">Need Help?</h3>
  <div class="call">Call Us: <b>555 - 014 - 9027</b></div>
  <div class="addr">Mon - Fri: 8.00 AM - 5.00 PM<br><br>Kelmora Wheel Academy<br>2180 Fernbrook Ct, Alder Falls<br>48372</div>
  <div class="social"><i></i><i></i><i></i><i></i></div>
  <div class="copy">&copy; 2019 Kelmora Wheel Academy</div>

  <h3 style="left:620px;top:67px">Send Your Query</h3>
  <div class="qfield" style="left:620px;top:140px;width:213px">Your Name</div>
  <div class="qfield" style="left:849px;top:140px;width:213px">Email</div>
  <div class="qfield" style="left:620px;top:194px;width:213px">Phone</div>
  <div class="qfield" style="left:849px;top:194px;width:213px">Your Query</div>
  <div class="qfield" style="left:620px;top:248px;width:442px;height:92px">Message</div>
  <span class="btn">Submit</span>
</footer>

</body>
</html>
```